I am a surgeon that operates on gynaecological cancer. Wish a design and logo for letter head.

Design should include my name: Dr. Torin Halwell, qualifications: FKMLTPVB, DMR. and state that I am a Gynaecological Oncologist and Advanced Laparoscopic Surgeon.
As for a logo. As all cancer is related to DNA, I think that that double helix could be used to symbolise a female shape, exaggerating the abdomen to suggest a mass.

Reason: Extended to view changes I have asked for.

```html
<!DOCTYPE html>
<html lang="en">
<head>
<meta charset="utf-8">
<title>Dr. Torin Halwell – Letterhead</title>
<link rel="stylesheet" href="https://fonts.googleapis.com/css2?family=Arimo:wght@400;700&display=swap">
<style>
  :root {
    --backdrop: #e6e7e9;
    --paper: #ffffff;
    --band-deep: #2a5cb0;
    --band-bright: #03a9ec;
    --band-end: #1d86d6;
    --gold: #f2b53b;
    --navy: #34348a;
    --ghost: #f3f3f4;
  }
  * { margin: 0; padding: 0; box-sizing: border-box; }
  html, body { width: 1200px; height: 1000px; overflow: hidden; }
  body {
    background: var(--backdrop);
    font-family: "Arimo", Arial, sans-serif;
    position: relative;
  }
  .sheet {
    position: absolute;
    left: 294px; top: 67px;
    width: 613px; height: 867px;
    background: var(--paper);
  }
  .header-band {
    position: absolute;
    left: 0; top: 49px;
    width: 100%; height: 70px;
    background: linear-gradient(90deg, var(--band-deep) 0%, var(--band-bright) 60%, var(--band-end) 100%);
  }
  .brand-dot {
    position: absolute;
    left: 316px; top: 71px;
    width: 26px; height: 26px;
    border-radius: 50%;
    background: var(--gold);
  }
  .doctor-name {
    position: absolute;
    right: 40px; top: 63px;
    color: var(--gold);
    font-weight: 700;
    font-size: 24px;
    line-height: 1;
    white-space: nowrap;
  }
  .qualifications {
    position: absolute;
    right: 41px; top: 98px;
    color: var(--gold);
    font-weight: 700;
    font-size: 9px;
    letter-spacing: 0.6px;
  }
  .specialty {
    position: absolute;
    right: 41px; top: 130px;
    text-align: right;
    color: var(--navy);
    font-size: 11px;
    line-height: 16px;
  }
  .specialty .line-one { letter-spacing: 2.4px; margin-right: -2.4px; }
  .specialty .line-two { letter-spacing: 0.2px; }
  .ghost-mark {
    position: absolute;
    left: 0; top: 430px;
    width: 100%;
    text-align: center;
    color: var(--ghost);
    font-weight: 700;
    font-size: 44px;
  }
</style>
</head>
<body>
  <div class="sheet">
    <div class="header-band"></div>
    <div class="brand-dot"></div>
    <div class="doctor-name">Dr. Torin Halwell</div>
    <div class="qualifications">FKMLTPVB, DMR.</div>
    <div class="specialty">
      <div class="line-one">Gynaecological Oncologist</div>
      <div class="line-two">and Advanced Laparoscopic Surgeon</div>
    </div>
    <div class="ghost-mark">Torin Halwell</div>
  </div>
</body>
</html>
```